BWK Business Card

A double sided business card based on your "Brightwater Keystone Ltd" Logo. To use the "BWK" logo on 1 side and the full company logo on the reverse.

Detials to be included:

Name: Tom Pellow
Postion: Consultant Orthotist & Expert Witness
T: +44 (0) 7958 302146
F: +44 (0) 7465 8810

```html
<!DOCTYPE html>
<html lang="en">
<head>
<meta charset="utf-8">
<title>BWK Business Card</title>
<link href="https://fonts.googleapis.com/css2?family=Cinzel:wght@400;600&family=Crimson+Text:wght@400;700&display=swap" rel="stylesheet">
<style>
  :root {
    --navy: #0b3a6e;
    --grey: #9a9a9a;
    --text-grey: #8c8c8c;
    --ink: #333a44;
    --card: #ffffff;
    --backdrop: #e9e7e3;
  }
  * { box-sizing: border-box; margin: 0; padding: 0; }
  html, body { width: 1200px; height: 720px; overflow: hidden; }
  body {
    background: var(--backdrop);
    font-family: "Crimson Text", Georgia, serif;
    position: relative;
  }
  .card {
    position: absolute;
    top: 200px;
    width: 540px;
    height: 310px;
    background: var(--card);
    box-shadow: 0 2px 10px rgba(0,0,0,0.12);
    overflow: hidden;
  }
  .card--front { left: 50px; }
  .card--back { left: 610px; display: flex; align-items: center; justify-content: center; }

  .front-band { position: absolute; left: 0; top: 0; }
  .front-mark {
    position: absolute;
    left: 30px; top: 70px;
    width: 120px;
    text-align: center;
    font-family: "Cinzel", Georgia, serif;
    font-weight: 600;
    font-size: 34px;
    letter-spacing: 2px;
    color: var(--navy);
  }
  .divider {
    position: absolute;
    left: 178px; top: 24px;
    width: 1px; height: 96px;
    background: var(--grey);
  }
  .company {
    position: absolute;
    left: 192px; top: 28px;
    font-family: "Cinzel", Georgia, serif;
    font-weight: 600;
    color: var(--navy);
    font-size: 22px;
    line-height: 1.05;
    text-transform: uppercase;
  }
  .tagline {
    position: absolute;
    left: 192px; top: 88px;
    font-family: "Cinzel", Georgia, serif;
    font-size: 9px;
    letter-spacing: 0.3px;
    color: var(--navy);
    text-transform: uppercase;
    border-bottom: 1px solid var(--grey);
    padding-bottom: 3px;
  }
  .person {
    position: absolute;
    right: 26px; top: 30px;
    text-align: right;
  }
  .person-name { font-weight: 700; font-size: 18px; color: var(--navy); }
  .person-role { font-size: 14px; color: var(--text-grey); line-height: 1.15; }

  .contact {
    position: absolute;
    left: 192px; top: 178px;
    list-style: none;
    font-size: 13.5px;
    color: var(--ink);
    line-height: 1.45;
  }
  .contact li { display: flex; align-items: center; gap: 6px; }
  .contact svg { width: 11px; height: 11px; fill: var(--navy); flex: none; }
  .contact .address { margin-top: 8px; padding-left: 0; }

  .back-mark {
    font-family: "Cinzel", Georgia, serif;
    font-weight: 600;
    font-size: 110px;
    letter-spacing: 10px;
    color: var(--navy);
  }
</style>
</head>
<body>
  <section class="card card--front" aria-label="Business card front">
    <svg class="front-band" width="175" height="310" viewBox="0 0 175 310" aria-hidden="true">
      <path d="M0 0 H60 V18 H80 V40 H160 V150 H20 V160 H165 V310 H0 Z" fill="var(--navy)"/>
      <rect x="20" y="40" width="140" height="110" fill="var(--card)"/>
      <line x1="171" y1="160" x2="171" y2="310" stroke="var(--grey)" stroke-width="1"/>
    </svg>
    <div class="front-mark">BWK</div>
    <div class="divider"></div>
    <h1 class="company">Brightwater<br>Keystone Ltd</h1>
    <p class="tagline">Excellence in Medical Legal Reporting</p>

    <div class="person">
      <p class="person-name">Tom Pellow</p>
      <p class="person-role">Consultant Orthotist<br>Expert Witness</p>
    </div>

    <ul class="contact">
      <li>
        <svg viewBox="0 0 12 12"><path d="M2.5 0.8 4.3 2.6 3.3 4.1c.7 1.6 1.9 2.8 3.6 3.6l1.5-1 1.8 1.8-1.3 1.9C5 10 1.9 7 0.6 2.1Z"/></svg>
        +44 (0) 7958 302146
      </li>
      <li>
        <svg viewBox="0 0 12 12"><rect x="1" y="5" width="10" height="6" rx="1"/><rect x="3" y="1" width="6" height="4"/></svg>
        +44 (0) 7465 8810
      </li>
      <li>
        <svg viewBox="0 0 12 12"><path d="M0.5 2.5h11v7h-11Z M1 3l5 3.5L11 3" stroke="#fff" stroke-width="0.8"/></svg>
        tom@brightwaterkeystone.co.uk
      </li>
      <li class="address">18 Alder Row Kingsbridge, Surrey, KT4 2RN</li>
    </ul>
  </section>

  <section class="card card--back" aria-label="Business card back">
    <p class="back-mark">BWK</p>
  </section>
</body>
</html>
```